Cleaning service website design

We need a new nice web design(logo will be the same) for a new cleaning service Company:

Informations about Company and logo you can take from flyers in attachments.

This is a cleaning service Company which have simple rules and we would like to show that(in checklist form) on website:

- What we do and that we're Cleaning Green

- Why us?

- How much(our pricing is simple)

Also we would like to communicate with clients by some nice/big pictures on website and the most important thing is our phone number and short/fast Freestimate.

Also there should be some space for description about our Company.

Generally all information on main page can be short: about us, about service(what we do), last reviews, tips (for example: Tip of the week) and other can be some introduction to subpage where will be more information.

There will be few subpages like: About us, About our service, Photos(Before and after), Reviews , Tips, FAQ, Contact, Looking for a Job? - most of them will be just text so you can project just one example.

```html
<!DOCTYPE html>
<html lang="en">
<head>
<meta charset="utf-8">
<title>Tidy Nest House Cleaning</title>
<link rel="stylesheet" href="https://fonts.googleapis.com/css2?family=Cabin:wght@400;500;600&family=Arimo:ital,wght@0,400;1,400&family=Dancing+Script:wght@600&display=swap">
<style>
:root{
  --navy:#0c215e;
  --blue:#0b5db0;
  --nav-blue:#0b4d9c;
  --green:#4a9b34;
  --green-light:#6cc24a;
  --text:#444;
  --panel:#f3f9fd;
  --panel-border:#cfe3f1;
  --white:#fff;
}
*{margin:0;padding:0;box-sizing:border-box}
html,body{width:1031px;height:1200px;overflow:hidden}
body{background:var(--navy);font-family:"Arimo",sans-serif;position:relative;color:var(--text)}
.page{position:absolute;left:77px;top:19px;width:877px;height:971px;background:var(--white)}
.brand{position:absolute;left:12px;top:36px;font-family:"Cabin",sans-serif;white-space:nowrap}
.brand-name{display:block;font-size:30px;font-weight:600;color:var(--green);line-height:1}
.brand-sub{display:block;font-size:12px;color:var(--blue);margin-top:6px;padding-left:2px}
.contact{position:absolute;top:37px;display:flex;align-items:center;gap:10px;font-family:"Cabin",sans-serif;white-space:nowrap}
.contact small{display:block;font-size:14px;color:#333}
.contact strong{display:block;font-size:22px;font-weight:500;line-height:1.1}
.call{left:455px}.call strong{color:var(--green);letter-spacing:1px}
.estimate{left:687px}.estimate strong{color:var(--blue)}
.nav{position:absolute;left:8px;top:130px;width:861px;height:44px;display:flex;background:linear-gradient(#1466bd,var(--nav-blue));border-radius:3px;overflow:hidden}
.nav a{display:flex;align-items:center;justify-content:center;white-space:nowrap;color:#fff;font-family:"Cabin",sans-serif;font-weight:600;font-size:12px;letter-spacing:.5px;text-decoration:none;border-right:1px solid #0a3f80;flex:0 0 auto}
.nav a.active{background:linear-gradient(#6cc24a,#3f9a2c)}
.nav a:last-child{border:none}
.slider{position:absolute;left:8px;top:183px;width:861px;height:286px;background:#ececec;border:1px solid #ddd;border-radius:3px}
.slide{position:absolute;left:8px;top:8px;width:843px;height:269px;background:#f2efe8;overflow:hidden}
.slide-photo{position:absolute;left:0;top:0;width:640px;height:269px;background:linear-gradient(90deg,#8a6d4a,#d8c6a8 45%,#c9b9a0 75%,#f2efe8)}
.tagline{position:absolute;left:612px;top:32px;white-space:nowrap}
.tagline .script{font-family:"Dancing Script",cursive;color:var(--blue);font-size:42px;line-height:1}
.tagline .plain{font-family:"Cabin",sans-serif;color:var(--green);font-size:26px;margin:8px 0 4px}
.tagline .right{padding-left:72px}
.dots{position:absolute;right:18px;bottom:14px;display:flex;gap:14px}
.dots span{width:13px;height:13px;border-radius:50%;background:#999;box-shadow:inset 0 1px 2px #555}
.dots span:first-child{background:#333}
.intro{position:absolute;left:10px;top:498px;width:594px}
h1{font-family:"Cabin",sans-serif;font-weight:500;color:var(--green);font-size:23px}
h2{font-family:"Cabin",sans-serif;font-weight:500;color:var(--blue);font-size:18px;margin:6px 0 10px;letter-spacing:.5px}
.intro p,.tip p{font-size:11.5px;line-height:19.6px;margin-bottom:7px;text-align:justify}
.rule{position:absolute;left:10px;top:692px;width:594px;border-top:1px solid #ccc}
h3{font-family:"Cabin",sans-serif;font-weight:500;color:var(--blue);font-size:19px}
.tip{position:absolute;left:10px;top:713px;width:594px}
.tip-text{width:379px;margin-top:13px}
.tip .lead{color:var(--green)}
.tip-photo{position:absolute;left:392px;top:39px;width:202px;height:113px;border:1px solid #ccc;padding:6px;background:#eee}
.tip-photo div{width:100%;height:100%;background:linear-gradient(90deg,#9a9186,#2d5cb8 45%,#3a66c2 55%,#a59b8c)}
.newsletter{position:absolute;left:10px;top:891px;width:594px;height:72px;background:linear-gradient(#6e8fc0,#4d6da3);border-radius:3px;display:flex;align-items:center;padding-left:23px}
.newsletter .label{font-family:"Cabin",sans-serif;color:#fff;font-size:23px;margin:0 26px 0 18px;white-space:nowrap}
.newsletter .field{width:260px;height:36px;background:#fff;border:1px solid #aab;font-size:12.5px;color:#555;padding:10px 14px}
.newsletter .submit{margin-left:7px;width:84px;height:35px;background:linear-gradient(#f4f4f4,#cfcfcf);border:1px solid #999;font-family:"Cabin",sans-serif;font-size:18px;color:#555;letter-spacing:1px;display:flex;align-items:center;justify-content:center}
.card{position:absolute;left:630px;width:237px;background:var(--panel);border:1px solid var(--panel-border);border-radius:3px;padding:16px 18px}
.card h3{font-size:18px;margin-bottom:10px}
.todo{top:501px;height:232px}
.todo li{list-style:none;display:flex;gap:10px;font-family:"Cabin",sans-serif;font-weight:500;color:var(--green);font-size:13.5px;line-height:19.5px;margin-bottom:9px}
.todo li svg{flex:0 0 14px;margin-top:3px}
.todo .art{position:absolute;right:10px;top:140px;width:74px;height:76px;border-radius:10px;background:linear-gradient(135deg,#f5c631,#6d4bb0 45%,#2a88d0)}
.reviews{top:743px;height:212px}
.reviews .chev{position:absolute;right:16px;top:20px}
.reviews blockquote{font-style:italic;font-size:11.5px;line-height:21.5px;text-align:justify;color:#444;padding:0 2px}
.reviews cite{display:block;font-style:normal;font-family:"Cabin",sans-serif;font-weight:500;color:var(--green);font-size:14px;margin-top:8px}
.footer-links{position:absolute;top:1010px;width:170px}
.footer-links h4{font-family:"Cabin",sans-serif;font-weight:400;color:var(--green-light);font-size:14px;margin-bottom:13px}
.footer-links li{list-style:none;color:#d0d8ea;font-family:"Cabin",sans-serif;font-size:12px;margin-bottom:8.4px;white-space:nowrap}
.footer-links li::before{content:"» ";margin-right:4px}
.footer-sep{position:absolute;left:758px;top:1013px;height:110px;border-left:1px solid #4a3a3a}
.footer-brand{position:absolute;left:852px;top:1028px;font-family:"Cabin",sans-serif;font-size:18px;font-weight:600;color:#9db0da;white-space:nowrap}
.join{position:absolute;left:790px;top:1091px;display:flex;align-items:center;gap:9px;color:#d0d8ea;font-family:"Cabin",sans-serif;font-size:12px;white-space:nowrap}
.join span.circle{width:22px;height:22px;border-radius:50%;background:#5d78b8}
.bottom{position:absolute;left:0;top:1145px;width:1031px;height:55px;background:#142d6e;text-align:center;line-height:50px;color:#a7b4d4;font-family:"Cabin",sans-serif;font-size:12px}
</style>
</head>
<body>
<div class="page">
  <div class="brand"><span class="brand-name">Tidy Nest</span><span class="brand-sub">house cleaning</span></div>
  <div class="contact call">
    <svg width="30" height="30" viewBox="0 0 30 30"><circle cx="15" cy="15" r="15" fill="#4a9b34"/><path d="M10 8c1-1 2 0 3 2s0 2-1 3c1 2 3 4 5 5 1-1 1-2 3-1s3 2 2 3c-1 2-3 3-6 1s-5-4-7-7-1-5 1-6z" fill="#fff"/></svg>
    <div><small>Call Us Today!</small><strong>555-014-2270</strong></div>
  </div>
  <div class="contact estimate">
    <svg width="26" height="30" viewBox="0 0 26 30"><rect x="1" y="1" width="24" height="28" rx="2" fill="#2a7cc8"/><rect x="4" y="4" width="18" height="6" fill="#fff"/><g fill="#fff"><rect x="4" y="13" width="4" height="3"/><rect x="11" y="13" width="4" height="3"/><rect x="18" y="13" width="4" height="3"/><rect x="4" y="19" width="4" height="3"/><rect x="11" y="19" width="4" height="3"/><rect x="18" y="19" width="4" height="3"/><rect x="4" y="24" width="4" height="3"/><rect x="11" y="24" width="4" height="3"/><rect x="18" y="24" width="4" height="3"/></g></svg>
    <div><small>Click here for</small><strong>FREE ESTIMATE</strong></div>
  </div>
  <nav class="nav">
    <a class="active" style="width:78px">HOME</a><a style="width:94px">ABOUT US</a><a style="width:108px">OUR SERVICE</a><a style="width:138px">PHOTOS GALLERY</a><a style="width:82px">REVIEWS</a><a style="width:56px">TIPS</a><a style="width:56px">FAQ</a><a style="width:90px">CONTACT</a><a style="width:159px">LOOKING FOR A JOB?</a>
  </nav>
  <div class="slider">
    <div class="slide">
      <div class="slide-photo" role="img" aria-label="Smiling family with their dog relaxing on a sofa at home"></div>
      <div class="tagline">
        <div class="script">Affordably</div>
        <div class="plain">making your life</div>
        <div class="script right">Simpler</div>
      </div>
      <div class="dots"><span></span><span></span><span></span><span></span></div>
    </div>
  </div>
  <section class="intro">
    <h1>Halton Region House Cleaning Services</h1>
    <h2>HOUSE CLEANING...TIDY NEST!</h2>
    <p>We are Daniel and Marta Kowal and we have personally experienced the struggle of finding a reliable and affordable maid service. We understand how busy life can be and cleaning is one of the tasks that falls off the list when you're stretched too thin. We are here to help! Let Tidy Nest take care of the house cleaning so you can focus on the more important things in life.</p>
    <p>Halton, Burlington, Oakville and Milton residents can count on us to make your home sparkle from top to bottom!</p>
  </section>
  <div class="rule"></div>
  <section class="tip">
    <h3>Tip of the week</h3>
    <div class="tip-text">
      <p class="lead">Sed adipiscing est vitae est suscipit scelerisque. Aenean ullamcor-per tincidunt enim ut auctor.</p>
      <p>Mauris ultricies facilisis nulla, nec bibendum risus tincidunt ut. Integer metus diam, pretium at hendrerit eget, consequat a est. Donec sit amet dignissim nisi. Vestibulum nisi urna, accumsan eget erat et, aliquam placerat leo. Cras sit amet orci aliquam, ullamcorper metus nec.</p>
    </div>
    <div class="tip-photo"><div role="img" aria-label="Cleaner in a blue top and yellow gloves standing in a kitchen"></div></div>
  </section>
  <div class="newsletter">
    <svg width="36" height="26" viewBox="0 0 36 26"><rect x="1" y="1" width="34" height="24" fill="#fff"/><path d="M2 2l16 13L34 2M2 24l12-11M34 24L22 13" stroke="#5a7ab0" stroke-width="2" fill="none"/></svg>
    <span class="label">News letter</span>
    <div class="field">Enter your mail ID</div>
    <div class="submit">SUBMIT</div>
  </div>
  <aside class="card todo">
    <h3>What we do?</h3>
    <ul>
      <li><svg width="14" height="14" viewBox="0 0 14 14"><circle cx="7" cy="7" r="6" fill="none" stroke="#4a9b34" stroke-width="1.6"/><path d="M4 7l2.2 2.2L12 3" stroke="#4a9b34" stroke-width="2" fill="none"/></svg>Thoroughly clean your bath-rooms, kitchen, bedrooms and living areas</li>
      <li><svg width="14" height="14" viewBox="0 0 14 14"><circle cx="7" cy="7" r="6" fill="none" stroke="#4a9b34" stroke-width="1.6"/><path d="M4 7l2.2 2.2L12 3" stroke="#4a9b34" stroke-width="2" fill="none"/></svg>Mop or vacuum your floors</li>
      <li><svg width="14" height="14" viewBox="0 0 14 14"><circle cx="7" cy="7" r="6" fill="none" stroke="#4a9b34" stroke-width="1.6"/><path d="M4 7l2.2 2.2L12 3" stroke="#4a9b34" stroke-width="2" fill="none"/></svg>Dust surfaces</li>
      <li><svg width="14" height="14" viewBox="0 0 14 14"><circle cx="7" cy="7" r="6" fill="none" stroke="#4a9b34" stroke-width="1.6"/><path d="M4 7l2.2 2.2L12 3" stroke="#4a9b34" stroke-width="2" fill="none"/></svg>Collect garbage</li>
      <li><svg width="14" height="14" viewBox="0 0 14 14"><circle cx="7" cy="7" r="6" fill="none" stroke="#4a9b34" stroke-width="1.6"/><path d="M4 7l2.2 2.2L12 3" stroke="#4a9b34" stroke-width="2" fill="none"/></svg>Make beds</li>
    </ul>
    <div class="art" role="img" aria-label="Cleaning bucket and spray bottle"></div>
  </aside>
  <aside class="card reviews">
    <h3>Last Reviews</h3>
    <svg class="chev" width="10" height="14" viewBox="0 0 10 14"><path d="M2 1l6 6-6 6" stroke="#999" stroke-width="2" fill="none"/></svg>
    <blockquote><b style="color:#0b5db0;font-style:normal">“</b>&nbsp; Etiam augue turpis, interdum ac adipiscing ac, accumsan eget turpis. Aliquam erat volutpat. Phasellus mi massa, congue feugiat purus eget, placerat pulvinar metus. <b style="color:#0b5db0;font-style:normal">”</b></blockquote>
    <cite>Client name, City</cite>
  </aside>
</div>

<div class="footer-links" style="left:80px"><h4>Quick Links</h4><ul><li>Etiam cursus magna</li><li>Nulla vestibulum</li><li>Interdum et malesuada</li><li>Nam eget</li></ul></div>
<div class="footer-links" style="left:250px"><h4>Quick Links</h4><ul><li>Etiam cursus magna</li><li>Nulla vestibulum</li><li>Interdum et malesuada</li><li>Nam eget</li></ul></div>
<div class="footer-links" style="left:430px"><h4>Quick Links</h4><ul><li>Etiam cursus magna</li><li>Nulla vestibulum</li><li>Interdum et malesuada</li><li>Nam eget</li></ul></div>
<div class="footer-links" style="left:600px"><h4>Quick Links</h4><ul><li>Etiam cursus magna</li><li>Nulla vestibulum</li><li>Interdum et malesuada</li><li>Nam eget</li></ul></div>
<div class="footer-sep"></div>
<div class="footer-brand">Tidy Nest</div>
<div class="join">Join with us :<span class="circle"></span><span class="circle"></span><span class="circle"></span></div>
<footer class="bottom">Copyright © &nbsp;2013 &nbsp;LONDON 2013. &nbsp;&nbsp;&nbsp;All rights reserved.</footer>
</body>
</html>
```